Quvanta Redesign

We need a face lift for our website, www.quvanta.com. We sell flooring and related products nationwide. We are interested in expanding the width of the website and introducing grays and black. We want the design to be both contemporary and user friendly.

```html
<!DOCTYPE html>
<html lang="en">
<head>
<meta charset="utf-8">
<title>Quvanta – Flooring</title>
<link href="https://fonts.googleapis.com/css2?family=Oxygen:wght@400;700&family=Oswald:wght@400;500;600&display=swap" rel="stylesheet">
<style>
:root{
  --ink:#2b2b2b;
  --text:#333;
  --red:#d0121b;
  --red-dark:#b50e16;
  --white:#fff;
  --orange:#f7a400;
  --footer:#4a4a4a;
}
*{box-sizing:border-box;margin:0;padding:0}
html,body{width:1200px;height:1146px;overflow:hidden}
body{position:relative;background:var(--white);font-family:"Oxygen",sans-serif;color:var(--text)}
a{color:inherit;text-decoration:none}
.abs{position:absolute}

.topbar{left:0;top:0;width:1200px;height:30px;background:var(--ink)}
.topbar nav{position:absolute;right:90px;top:7px;font-size:13.5px;color:#eee}
.topbar nav span{margin:0 9px;color:#aaa}

.header-bg{left:0;top:30px;width:1200px;height:226px;background:linear-gradient(#fafafa,#e6e6e6);border-bottom:4px solid #cfcfcf}

.brand{left:74px;top:52px;display:flex;align-items:center;gap:8px}
.brand .mark{width:30px;height:30px;background:var(--red)}
.brand .name{font-size:36px;font-weight:700;color:var(--red);letter-spacing:-.5px}
.tagline{left:118px;top:99px;font-size:10px;font-weight:700;color:var(--ink)}

.phone{right:95px;top:50px;display:flex;align-items:center;gap:12px;font-size:20px;color:#444}
.cart{left:749px;top:96px;display:flex;align-items:center;gap:10px;font-size:13px;color:#777}
.cart .icon{width:28px;height:28px;border-radius:50%;background:#ddd;display:flex;align-items:center;justify-content:center}
.cart .badge{position:absolute;left:90px;top:-4px;width:15px;height:15px;border-radius:50%;background:var(--red);color:#fff;font-size:9px;text-align:center;line-height:15px;font-weight:700}
.search{left:879px;top:99px;width:194px;height:25px;border:1px solid #ccc;background:#fff;font-size:12px;font-style:italic;color:#888;padding:5px 11px}
.search-btn{left:1083px;top:99px;width:27px;height:25px;background:var(--red);display:flex;align-items:center;justify-content:center}

.mainnav{left:75px;top:137px;width:1050px;height:40px;background:linear-gradient(#fafafa,#dcdcdc);border-bottom:1px solid #bbb;display:flex}
.mainnav a{font-size:14.5px;color:#333;line-height:40px;padding:0 15px;border-right:1px solid #c8c8c8;flex:auto;text-align:center}
.mainnav a:last-child{border-right:0}
.corner{top:177px;width:0;height:0;border-top:10px solid var(--red-dark)}
.corner.l{left:75px;border-left:15px solid transparent;transform:scaleX(-1)}
.corner.r{left:1110px;border-left:15px solid transparent}

.stage{left:91px;top:177px;width:1020px;height:397px;background:#fff;box-shadow:0 1px 2px rgba(0,0,0,.15)}
.stage-shadow{left:52px;top:568px;width:1098px;height:10px;background:radial-gradient(ellipse at center,rgba(0,0,0,.3),rgba(0,0,0,0) 70%)}

.sidebar{left:99px;top:185px;width:245px;height:384px;background:var(--red);padding:12px 8px}
.side-head{background:#fff;height:28px;border-radius:3px;display:flex;justify-content:space-between;align-items:center;padding:0 12px;color:var(--red);font-weight:700;font-size:16px}
.side-list{background:#f4f4f4;margin-top:6px;border-radius:3px;height:120px;padding:10px 0 0 16px;display:grid;grid-template-columns:104px 100px;grid-auto-rows:26px;font-size:13px;color:#444}
.side-list span::before{content:"›";color:var(--red);font-weight:700;margin-right:8px;font-size:16px}
.side-btn{margin-top:17px;height:29px;border:1px solid #f27c80;border-radius:3px;display:flex;justify-content:space-between;align-items:center;padding:0 12px;color:#fff;font-weight:700;font-size:16px}

.hero{left:357px;top:185px;width:746px;height:384px;background:linear-gradient(180deg,#5b5a4a 0%,#8a8062 45%,#a47a4a 75%,#c39363 100%)}
.hero-title{left:357px;top:505px;width:746px;text-align:center;font-family:"Oswald",sans-serif;font-weight:600;font-size:35px;color:#111}
.arrow-btn{top:366px;width:33px;height:33px;border-radius:50%;background:#fff;display:flex;align-items:center;justify-content:center;font-size:20px;font-weight:700;color:#333}

.box{left:98px;width:241px;background:#fff;border:1px solid #ddd;border-top:3px solid var(--red)}
.box h3{font-family:"Oswald",sans-serif;font-weight:400;font-size:23px;color:#333;text-align:center}
.newsletter{top:611px;height:158px}
.newsletter .dark{position:absolute;left:-6px;top:42px;width:251px;height:104px;background:linear-gradient(#3a3a3a,#777);color:#fff;font-size:13px;font-weight:700;padding:16px 16px;line-height:18px}
.newsletter .field{position:absolute;left:16px;top:63px;width:220px;height:24px;background:#fff;font-size:11.5px;color:#444;padding:5px 10px;font-weight:400}
.newsletter .sub{position:absolute;left:136px;top:0;width:84px;height:24px;background:var(--orange);color:#222;text-align:center;line-height:24px;font-size:12.5px}
.payment{top:789px;height:120px}
.pay-row{display:flex;gap:9px;justify-content:center;margin-top:12px}
.pay-row i{display:block;width:32px;height:20px;border-radius:2px;background:#dfe4ea;border:1px solid #c9d0d8}

.card{top:611px;width:235px;height:209px;border:1px solid #ccc;background:#fff;padding:10px}
.card .photo{width:100%;height:187px}
.ribbon{top:607px;width:78px;height:78px;overflow:hidden}
.ribbon div{position:absolute;left:-28px;top:20px;width:120px;height:34px;background:var(--red);transform:rotate(-45deg);color:#fff;text-align:center;font-weight:700;font-size:18px;line-height:20px}
.ribbon small{display:block;font-size:9px;line-height:10px}
.prod-name{top:827px;width:240px;font-size:16.5px;font-weight:700;color:#333;line-height:20px}
.btn-cart{top:879px;width:120px;height:31px;border:1px solid #aaa;border-radius:3px;background:linear-gradient(#f7f7f7,#cfcfcf);font-weight:700;font-size:13.5px;color:#444;text-align:center;line-height:29px}
.details{top:887px;font-size:13.5px;color:var(--red);text-decoration:underline}

.footer{left:0;top:978px;width:1200px;height:104px;background:var(--footer);color:#eee;font-size:13.5px}
.footer p{position:absolute;left:100px}
.footer span{margin:0 9px;color:#bbb}
.seal{top:1007px;height:50px;background:#e8e8e8;border-radius:3px}
.partner{height:46px;background:#e3e3e3;border-radius:4px}
</style>
</head>
<body>

<div class="abs topbar"><nav><a href="#">My Account</a><span>|</span><a href="#">FAQ</a><span>|</span><a href="#">Order Tracking</a></nav></div>
<div class="abs header-bg"></div>

<div class="abs brand"><div class="mark"></div><div class="name">Quvanta</div></div>
<div class="abs tagline">Quality Floors Since '99</div>

<div class="abs phone">
  <svg width="20" height="20" viewBox="0 0 24 24"><path fill="#555" d="M6.6 10.8c1.4 2.8 3.8 5.1 6.6 6.6l2.2-2.2c.3-.3.7-.4 1-.2 1.1.4 2.3.6 3.6.6.6 0 1 .4 1 1V20c0 .6-.4 1-1 1C10.6 21 3 13.4 3 4c0-.6.4-1 1-1h3.5c.6 0 1 .4 1 1 0 1.3.2 2.5.6 3.6.1.3 0 .7-.2 1z"/></svg>
  1-800-555-0148
</div>

<div class="abs cart">
  <div class="icon"><svg width="16" height="14" viewBox="0 0 16 14"><path fill="#555" d="M0 1h3l2 8h8l2-6H5" stroke="#555" stroke-width="1.5"/><circle cx="6" cy="12" r="1.4" fill="#555"/><circle cx="12" cy="12" r="1.4" fill="#555"/></svg></div>
  My Cart<div class="badge">1</div>
</div>
<div class="abs search">Search here</div>
<div class="abs search-btn"><svg width="14" height="14" viewBox="0 0 14 14"><circle cx="6" cy="6" r="4.2" fill="none" stroke="#fff" stroke-width="2"/><path d="M9 9l4 4" stroke="#fff" stroke-width="2.2"/></svg></div>

<nav class="abs mainnav">
  <a href="#">LAMINATE</a><a href="#">HARDWOOD</a><a href="#">AREA RUGS</a><a href="#">BAMBOO</a><a href="#">CORK</a><a href="#">VINYL</a><a href="#">CARPET TILE</a><a href="#">TILE</a><a href="#">CLOCKS</a><a href="#">BATH</a><a href="#">CLEARANCE</a>
</nav>
<div class="abs corner l"></div><div class="abs corner r"></div>

<div class="abs stage-shadow"></div>
<div class="abs stage"></div>

<aside class="abs sidebar">
  <div class="side-head">Shop By Brand<svg width="12" height="8" viewBox="0 0 12 8"><path d="M1 1l5 5 5-5" fill="none" stroke="#d0121b" stroke-width="2.4"/></svg></div>
  <div class="side-list"><span>Laminate</span><span>Vinyl</span><span>Hardwood</span><span>Carpet Tile</span><span>Bamboo</span><span>Tile</span><span>Cork</span></div>
  <div class="side-btn">Home Decor<span>›</span></div>
  <div class="side-btn">Accessories<span>›</span></div>
  <div class="side-btn">Flooring Facts<span>›</span></div>
  <div class="side-btn">Recently Viewed<span>›</span></div>
</aside>

<div class="abs hero" role="img" aria-label="Modern living room with cream sectional sofa, wall fireplace, city view window and light hardwood floor"></div>
<div class="abs hero-title">BEST FLOORING SOLUTIONS</div>
<div class="abs arrow-btn" style="left:368px">‹</div>
<div class="abs arrow-btn" style="left:1059px">›</div>

<section class="abs box newsletter">
  <h3 style="margin-top:6px">Join Our Newsletter</h3>
  <div class="dark">Stay Up-to-date With Special<br>Events And Happenings
    <div class="field">email address<div class="sub">Subscribe</div></div>
  </div>
</section>

<section class="abs box payment">
  <h3 style="margin-top:5px">Payment Options</h3>
  <div class="pay-row"><i></i><i></i><i></i><i></i></div>
  <div class="pay-row"><i></i><i style="width:72px"></i></div>
</section>

<div class="abs card" style="left:358px"><div class="photo" role="img" aria-label="Living room with armchair and light laminate flooring" style="background:linear-gradient(#9aa08a,#c9b08a)"></div></div>
<div class="abs card" style="left:617px"><div class="photo" role="img" aria-label="Foyer with staircase and beige stone-look vinyl tile" style="background:linear-gradient(#5a4a3a,#d8c8b4)"></div></div>
<div class="abs card" style="left:876px"><div class="photo" role="img" aria-label="Den with stone fireplace, red ottoman and acacia hardwood floor" style="background:linear-gradient(#8a7560,#6a3a22)"></div></div>

<div class="abs ribbon" style="left:354px"><div>2.49<small>sq.ft</small></div></div>
<div class="abs ribbon" style="left:613px"><div>3.79<small>sq.ft</small></div></div>
<div class="abs ribbon" style="left:872px"><div>4.99<small>sq.ft</small></div></div>

<div class="abs prod-name" style="left:361px">Harlow Seaside Oak</div>
<div class="abs prod-name" style="left:618px">Bellmark Stoneform<br>Luxury Vinyl</div>
<div class="abs prod-name" style="left:878px">Harlow Timberline<br>Acacia Hardwood</div>

<div class="abs btn-cart" style="left:359px">ADD TO CART</div>
<div class="abs details" style="left:532px">Details</div>
<div class="abs btn-cart" style="left:617px">ADD TO CART</div>
<div class="abs details" style="left:790px">Details</div>
<div class="abs btn-cart" style="left:881px">ADD TO CART</div>
<div class="abs details" style="left:1054px">Details</div>

<footer class="abs footer">
  <p style="top:20px">About Us<span>|</span>Careers<span>|</span>Consumer Reviews<span>|</span>Contact Us<span>|</span>Faq</p>
  <p style="top:42px">Ordering<span>|</span>Pricing<span>|</span>Privacy Policy<span>|</span>Return Policy<span>|</span>Shipping<span>|</span>Sitemap</p>
  <p style="top:74px">© 2013 quvanta.<span>|</span>All Right Reserved</p>
</footer>
<div class="abs seal" style="left:785px;width:63px"></div>
<div class="abs seal" style="left:881px;width:102px"></div>
<div class="abs seal" style="left:1008px;width:103px;height:38px;top:1013px;background:#1f5d8c"></div>

<div class="abs partner" style="left:100px;top:1090px;width:104px"></div>
<div class="abs partner" style="left:971px;top:1095px;width:130px;height:44px"></div>

</body>
</html>
```